Newsletter Kellos-Track-Weeks

Hello i need some Newsletter to promote my company and the new events that we make.
we are organist motorbike events in different circuits in europe

please wrote me when you need some other format from the logo

I need a Template that include the text blocks. in the moment i don’t have finish the text.

we need the newsletter to send in sozialmedia, e-mail and homepage.
its always for online we don’t print and send newsletter.

i will send the newsletters with the program swift post

Target Market(s)

us target market are all motorbike stores and all motorbike riders.

Industry/Entity Type

Events

Requirements
Must have
• i don’t know :)
have to be us logo and see very cool and crazy..
My Homepage maybe can help
www.kellos-track-weeks.ch
Nice to have
• a link to my contact e-mail and web address

```html
<!DOCTYPE html>
<html lang="en">
<head>
<meta charset="utf-8">
<title>Kellos-Track-Weeks Newsletter</title>
<link rel="stylesheet" href="https://fonts.googleapis.com/css2?family=Arimo:wght@400;700&display=swap">
<style>
  :root {
    --page: #ffffff;
    --ink: #111111;
    --black: #070707;
    --red: #d10a00;
    --body-grey: #dcdcdc;
    --frame: #ffffff;
    --photo-dark: #2b3440;
    --photo-mid: #56606a;
    --photo-warm: #c9716a;
  }
  * { margin: 0; padding: 0; box-sizing: border-box; }
  html, body { width: 1200px; height: 1000px; overflow: hidden; background: var(--page); }
  body { position: relative; font-family: "Arimo", Arial, sans-serif; color: var(--ink); }

  .newsletter { position: absolute; left: 302px; top: 39px; width: 620px; height: 900px; background: var(--body-grey); }

  .masthead { position: absolute; left: 0; top: 0; width: 620px; height: 148px; background: var(--black); }
  .brand { position: absolute; left: 0; right: 0; top: 58px; display: flex; justify-content: center; align-items: center; gap: 12px; }
  .brand-square { width: 22px; height: 22px; background: var(--red); }
  .brand-name { color: #ffffff; font-weight: 700; font-size: 26px; }

  .issue-band { position: absolute; left: 0; top: 148px; width: 620px; height: 41px; background: var(--red); color: #fff; font-weight: 700; font-size: 18px; line-height: 41px; padding-left: 30px; }

  .recipient { position: absolute; left: 29px; top: 212px; font-weight: 700; font-size: 16px; }

  .story-heading { position: absolute; font-weight: 700; font-size: 18px; }
  .story-text { position: absolute; width: 280px; font-size: 11.6px; line-height: 18px; overflow: hidden; }
  .story-text p + p { margin-top: 18px; }

  .photo-frame { position: absolute; width: 265px; height: 228px; background: var(--frame); padding: 8px; }
  .photo { width: 100%; height: 100%; background: linear-gradient(135deg, var(--photo-dark) 0%, var(--photo-mid) 45%, var(--photo-warm) 70%, var(--photo-dark) 100%); }

  .story-one .story-heading { left: 28px; top: 274px; }
  .story-one .story-text { left: 29px; top: 309px; height: 180px; }
  .story-one .photo-frame { left: 331px; top: 278px; }

  .story-two .photo-frame { left: 27px; top: 542px; }
  .story-two .story-heading { left: 312px; top: 538px; }
  .story-two .story-text { left: 313px; top: 579px; height: 162px; }
  .read-more { position: absolute; left: 313px; top: 751px; color: var(--red); font-size: 12px; text-decoration: underline; }

  .footer { position: absolute; left: 0; top: 830px; width: 620px; height: 70px; background: var(--black); }
  .unsubscribe { position: absolute; left: 27px; top: 12px; width: 163px; height: 41px; background: var(--red); color: #fff; font-weight: 700; font-size: 16px; line-height: 41px; text-align: center; text-decoration: none; }
  .contact { position: absolute; right: 24px; top: 7px; text-align: right; font-size: 13px; line-height: 27px; }
  .contact a { color: var(--red); text-decoration: none; display: block; }
</style>
</head>
<body>
  <main class="newsletter">
    <header class="masthead">
      <div class="brand">
        <span class="brand-square"></span>
        <span class="brand-name">Kellos-Track-Weeks</span>
      </div>
    </header>

    <div class="issue-band">September 2014</div>

    <div class="recipient">To: Person of Interest</div>

    <section class="story-one">
      <h2 class="story-heading">Heading Here</h2>
      <div class="story-text">
        <p>Lorem ipsum dolor sit amet, consectetuer adipiscing elit, sed diam nonummy nibh euismod tincidunt ut laoreet dolore magna aliquam erat volutpat. Ut wisi enim ad minim veniam, quis nostrud exerci tation ullamcorper suscipit lobortis nisl ut aliquip ex ea commodo consequat.</p>
        <p>Duis autem vel eum iriure dolor in hendrerit in vulpu-tate velit esse molestie consequat, vel illum dolore eu feugiat nulla facilisis at vero eros et accumsan et</p>
      </div>
      <div class="photo-frame">
        <div class="photo" role="img" aria-label="Photo of a racer on an orange sport motorbike leaning into a track corner"></div>
      </div>
    </section>

    <section class="story-two">
      <div class="photo-frame">
        <div class="photo" role="img" aria-label="Photo of a racer on an orange sport motorbike leaning into a track corner"></div>
      </div>
      <h2 class="story-heading">Heading Here</h2>
      <div class="story-text">
        <p>Lorem ipsum dolor sit amet, consectetuer adipiscing elit, sed diam nonummy nibh euismod tincidunt ut laoreet dolore magna aliquam erat volutpat. Ut wisi enim ad minim veniam, quis nostrud exerci tation ullamcorper suscipit lobortis nisl ut aliquip ex ea commodo consequat.</p>
        <p>Duis autem vel eum iriure dolor in hendrerit in vulpu-tate velit esse molestie consequat, vel illum dolore</p>
      </div>
      <a class="read-more" href="#">Click here.</a>
    </section>

    <footer class="footer">
      <a class="unsubscribe" href="#">UNSUBSCRIBE</a>
      <div class="contact">
        <a href="mailto:info@kellos-track-weeks.ch">Email:info@kellos-track-weeks.ch</a>
        <a href="http://www.kellos-track-weeks.ch/">Website:http://www.kellos-track-weeks.ch/</a>
      </div>
    </footer>
  </main>
</body>
</html>
```